BrovaLT BIZ Card, email signature & Stationary

Professional business cards, email signatures and ms word letterhead

Target Market(s)

business owners

Industry/Entity Type

cloud hosting

Contact Information for Business Card

name title office phone number , direct line, fax email address web site

Font styles to use
Other font styles liked:
• something that compliments font in logo

```html
<!DOCTYPE html>
<html lang="en">
<head>
<meta charset="utf-8">
<title>BrovaLT Business Card</title>
<link rel="stylesheet" href="https://fonts.googleapis.com/css2?family=Montserrat:wght@700&family=Work+Sans:wght@300;400;500&display=swap">
<style>
  :root {
    --stage: #171717;
    --card: #111111;
    --card-edge: #1c1c1c;
    --red: #d81920;
    --white: #f2f2f2;
    --band: #e6e6e6;
    --ink: #1a1a1a;
    --muted: #d8d8d8;
  }
  * { margin: 0; padding: 0; box-sizing: border-box; }
  html, body {
    width: 1200px; height: 800px; overflow: hidden;
    background: var(--stage);
    font-family: "Work Sans", sans-serif;
  }
  .stage {
    position: relative; width: 1200px; height: 800px;
    display: flex; align-items: center; justify-content: center; gap: 50px;
  }
  .card {
    position: relative; width: 540px; height: 310px;
    border-radius: 22px; overflow: hidden;
    background: var(--card);
    box-shadow: 0 18px 40px rgba(0,0,0,.55), inset 0 0 0 1px var(--card-edge);
  }

  /* Back side */
  .card-back .pattern-field {
    position: absolute; inset: 0;
    background: linear-gradient(150deg, #0c0c0c 0%, #141414 45%, #3a3a3a 78%, #5a5a5a 100%);
  }
  .card-back .wordmark {
    position: absolute; left: 0; right: 0; bottom: 62px;
    text-align: center;
    font-family: "Work Sans", sans-serif; font-weight: 300;
    font-size: 50px; letter-spacing: 1px; color: var(--white);
  }

  /* Front side */
  .card-front .wordmark {
    position: absolute; left: 50px; top: 78px;
    font-family: "Work Sans", sans-serif; font-weight: 300;
    font-size: 54px; letter-spacing: 1px; color: var(--red);
  }
  .card-front .divider {
    position: absolute; left: 292px; top: 60px;
    width: 1px; height: 150px; background: var(--red);
  }
  .contact {
    position: absolute; left: 310px; top: 66px;
  }
  .contact .name {
    font-family: "Montserrat", sans-serif; font-weight: 700;
    font-size: 16px; color: var(--red); letter-spacing: .3px;
  }
  .contact .title {
    font-size: 12px; color: var(--muted); margin: 3px 0 10px;
  }
  .contact ul { list-style: none; }
  .contact li {
    display: flex; align-items: center; gap: 8px;
    font-size: 11.5px; color: var(--muted); line-height: 20px;
  }
  .contact svg { width: 12px; height: 12px; fill: var(--red); flex: none; }
  .address-band {
    position: absolute; left: 0; right: 0; bottom: 0; height: 30px;
    background: var(--band);
    display: flex; align-items: center; padding-left: 34px;
    font-size: 11px; font-weight: 500; color: var(--ink); letter-spacing: .3px;
  }
  .address-band .accent {
    position: absolute; right: 0; top: 0; bottom: 0; width: 92px;
    background: var(--red);
    border-left: 6px solid var(--card);
  }
</style>
</head>
<body>
<main class="stage">
  <section class="card card-back">
    <div class="pattern-field" role="img" aria-label="Repeating brand pattern in black and grey, fading lighter toward the lower right"></div>
    <div class="wordmark">BrovaLT</div>
  </section>

  <section class="card card-front">
    <div class="wordmark">BrovaLT</div>
    <div class="divider"></div>
    <div class="contact">
      <p class="name">Daniel Orvesk</p>
      <p class="title">Director Technical</p>
      <ul>
        <li>
          <svg viewBox="0 0 24 24"><path d="M6.6 10.8a15 15 0 0 0 6.6 6.6l2.2-2.2c.3-.3.7-.4 1-.2 1.1.4 2.3.6 3.6.6.6 0 1 .4 1 1V20c0 .6-.4 1-1 1A17 17 0 0 1 3 4c0-.6.4-1 1-1h3.5c.6 0 1 .4 1 1 0 1.3.2 2.5.6 3.6.1.3 0 .7-.2 1z"/></svg>
          +0418 552 307
        </li>
        <li>
          <svg viewBox="0 0 24 24"><path d="M7 1h10a2 2 0 0 1 2 2v18a2 2 0 0 1-2 2H7a2 2 0 0 1-2-2V3a2 2 0 0 1 2-2zm0 3v14h10V4zm5 15.5a1.2 1.2 0 1 0 0 2.4 1.2 1.2 0 0 0 0-2.4z"/></svg>
          +0418 552 307
        </li>
        <li>
          <svg viewBox="0 0 24 24"><path d="M2 5h20v14H2zm2 2v.5l8 5 8-5V7zm0 2.8V17h16V9.8l-8 5z"/></svg>
          daniel@brovalt.com
        </li>
        <li>
          <svg viewBox="0 0 24 24"><path d="M12 2a10 10 0 1 0 0 20 10 10 0 0 0 0-20zm6.9 6h-2.9a15 15 0 0 0-1.4-3.6A8 8 0 0 1 18.9 8zM12 4c.8 1.2 1.5 2.5 1.9 4h-3.8c.4-1.5 1.1-2.8 1.9-4zM4.3 14a8 8 0 0 1 0-4h3.4a16 16 0 0 0 0 4zm.8 2h2.9c.3 1.3.8 2.5 1.4 3.6A8 8 0 0 1 5.1 16zM8 8H5.1a8 8 0 0 1 4.3-3.6C8.8 5.5 8.3 6.7 8 8zm4 12c-.8-1.2-1.5-2.5-1.9-4h3.8c-.4 1.5-1.1 2.8-1.9 4zm2.3-6H9.7a14 14 0 0 1 0-4h4.6a14 14 0 0 1 0 4zm.3 5.6c.6-1.1 1.1-2.3 1.4-3.6h2.9a8 8 0 0 1-4.3 3.6zM16.3 14a16 16 0 0 0 0-4h3.4a8 8 0 0 1 0 4z"/></svg>
          www.brovalt.com
        </li>
      </ul>
    </div>
    <div class="address-band">
      2740 Halden Ave, Suite 310, Marlow, CA 90417
      <span class="accent"></span>
    </div>
  </section>
</main>
</body>
</html>
```